New signage for apartment community in the Pacific Northwest

Signage for an apartment community in the Pacific Northwest. It should have a contemporary northwest vibe with a fresh exciting feeling. We are open to the colors cayenne, white, charcoal and a splash of lime green. Sign to have the name 'VELTO' with the address number 28391 smaller underneath. sign can include a shape under the name or a feeling of energy in the shape of the name.

Target Market(s)

Young urban professionals

Industry/Entity Type

Real Estate Development

Requirements
Must have
• eyecatching
Should not have
• anything too cute or too busy

```html
<!DOCTYPE html>
<html lang="en">
<head>
<meta charset="utf-8">
<title>VELTO Monument Sign</title>
<link rel="stylesheet" href="https://fonts.googleapis.com/css2?family=Cormorant+Garamond:wght@500;600&display=swap">
<style>
  :root {
    --canvas: #eeeeee;
    --sign-face: #ffffff;
    --charcoal: #3a4754;
    --cayenne: #c4522e;
    --number: #ffffff;
  }
  html, body {
    margin: 0;
    padding: 0;
    width: 800px;
    height: 1200px;
    overflow: hidden;
    background: var(--canvas);
  }
  .canvas {
    position: relative;
    width: 800px;
    height: 1200px;
    display: flex;
    align-items: center;
    justify-content: center;
  }
  .monument-sign {
    width: 660px;
    height: auto;
    display: block;
    filter: drop-shadow(0 3px 6px rgba(0, 0, 0, 0.18));
  }
  .sign-face { fill: var(--sign-face); }
  .sign-base { fill: var(--charcoal); }
  .sign-accent-wave { fill: var(--cayenne); }
  .community-name {
    font-family: "Cormorant Garamond", "Times New Roman", serif;
    font-weight: 500;
    font-size: 118px;
    letter-spacing: 4px;
    fill: var(--charcoal);
  }
  .address-number {
    font-family: "Cormorant Garamond", "Times New Roman", serif;
    font-weight: 600;
    font-size: 42px;
    letter-spacing: 1px;
    fill: var(--number);
  }
</style>
</head>
<body>
  <main class="canvas">
    <svg class="monument-sign" viewBox="0 0 640 420" xmlns="http://www.w3.org/2000/svg" role="img" aria-label="VELTO community sign, address 28391">
      <path class="sign-face" d="M0,40 Q320,-22 640,40 L640,420 L0,420 Z"/>
      <path class="sign-base" d="M0,268 C110,305 220,342 330,330 C440,318 530,290 640,296 L640,420 L0,420 Z"/>
      <path class="sign-accent-wave" d="M0,254 C110,292 220,330 330,318 C440,306 530,278 640,284 L640,296 C530,290 440,318 330,330 C220,342 110,305 0,268 Z"/>
      <text class="community-name" x="320" y="205" text-anchor="middle">VELTO</text>
      <text class="address-number" x="320" y="392" text-anchor="middle">28391</text>
    </svg>
  </main>
</body>
</html>
```